A Maple Syrup Label for a Local Buniness

We are looking for a label for our maple syrup business. Our business currently sells honey, and we are expanding into maple syrup. Our Business name is "Corvale Bees" and we currently have a logo attached below. We would like to incorporate the bee and CB part, but the label could also read "Corvale Farms" with the words maple syrup. We do not want consumers to confuse the maple syrup jars with the honey jars. It should be clear that the jars contain maple syrup. We are open to new designs as well.

```html
<!DOCTYPE html>
<html lang="en">
<head>
<meta charset="utf-8">
<title>Corvale Farms Maple Syrup Label</title>
<link rel="stylesheet" href="https://fonts.googleapis.com/css2?family=Cinzel:wght@500;600&family=Playfair+Display:ital,wght@0,700;1,700&family=Libre+Franklin:wght@300;400;600;800&display=swap">
<style>
:root{
  --navy:#1b2a58;
  --blue:#1e5fae;
  --blue-deep:#0f2f6e;
  --gold:#f6c200;
  --parchment:#e7d0a0;
  --parchment-warm:#dfbe8c;
  --cream:#f3e3a2;
  --red:#c2242f;
  --ink:#111;
}
*{margin:0;padding:0;box-sizing:border-box}
html,body{width:1200px;height:676px;overflow:hidden;background:#fff}
.canvas{position:relative;width:1200px;height:676px}
.label-shape{position:absolute;left:0;top:0}
.abs{position:absolute}

/* nutrition panel */
.nutrition{left:164px;top:222px;width:174px;height:232px;background:#fff;border:2px solid var(--ink);padding:3px 6px;font-family:"Libre Franklin",Arial,sans-serif;color:var(--ink);overflow:hidden}
.nutrition h2{font-weight:800;font-size:19px;line-height:20px;letter-spacing:-.2px;border-bottom:1px solid var(--ink);padding-bottom:1px}
.nutrition .servings{font-weight:300;font-size:9px;line-height:11px;margin-top:2px}
.nutrition .row{display:flex;justify-content:space-between;font-size:9px;line-height:12px}
.nutrition .bar-thick{height:7px;background:var(--ink);margin:2px 0 3px}
.nutrition .amount{font-weight:600;font-size:9.5px;line-height:11px;padding-left:2px}
.nutrition .calories{display:flex;justify-content:space-between;font-weight:800;font-size:19px;line-height:19px;padding-left:2px;border-bottom:4px solid var(--ink);padding-bottom:1px}
.nutrition .dv{text-align:right;font-size:4.5px;line-height:6px;border-bottom:1px solid var(--ink)}
.nutrition .line{display:flex;justify-content:space-between;font-size:9px;line-height:13.5px;border-bottom:1px solid var(--ink);padding-right:6px}
.nutrition .line b{font-weight:600}
.nutrition .line.sub{padding-left:26px;font-weight:300}
.nutrition .line.last{border-bottom:4px solid var(--ink);line-height:18px}
.nutrition .foot{font-size:5.8px;line-height:8px;padding:3px 0 2px;border-bottom:1px solid var(--ink)}
.nutrition .ingredients{font-size:9px;line-height:12px;padding:3px 0 0 2px}

.order-note{left:345px;top:428px;transform:rotate(-90deg);transform-origin:left top;font-family:"Libre Franklin",Arial,sans-serif;font-size:8px;line-height:9px;color:var(--red);font-weight:600;white-space:nowrap}
.order-note span{display:block;font-weight:400;color:var(--navy)}
.recycle{left:354px;top:299px;width:15px;height:15px}

/* centre panel */
.brand-mark{left:505px;top:225px;width:200px;display:flex;align-items:center;justify-content:center;gap:8px;font-family:"Cinzel",Georgia,serif;font-weight:600;font-size:24px;color:var(--navy);white-space:nowrap}
.brand-mark i{display:block;width:14px;height:14px;border-radius:50%;background:var(--gold)}
.title{left:395px;width:420px;text-align:center;font-family:"Cinzel",Georgia,serif;font-weight:500;white-space:nowrap}
.title.farm{top:318px;font-size:40px;line-height:44px;color:var(--navy);letter-spacing:-.5px}
.title.product{top:360px;font-size:41px;line-height:44px;color:var(--red)}

.ticket{left:424px;top:413px;width:361px;height:93px;background:var(--cream);clip-path:polygon(0 0,100% 0,98% 12%,100% 24%,98% 36%,100% 48%,98% 60%,100% 72%,98% 84%,100% 100%,50% 100%,0 100%,2% 84%,0 72%,2% 60%,0 48%,2% 36%,0 24%,2% 12%)}
.ticket-frame{left:435px;top:423px;width:339px;height:79px;border:1.5px solid var(--ink)}
.ticket-divider-v{left:660px;top:423px;width:1.5px;height:79px;background:var(--ink)}
.ticket-divider-h{left:435px;top:480px;width:226px;height:1.5px;background:var(--ink)}
.ticket-text{left:443px;top:428px;width:208px;font-family:"Playfair Display",Georgia,serif;font-style:italic;font-weight:700;font-size:10.5px;line-height:10.5px;color:var(--navy);text-align:justify;letter-spacing:-.2px}
.ticket-text em{color:var(--red)}
.ticket-url{left:455px;top:484px;font-family:"Playfair Display",Georgia,serif;font-style:italic;font-weight:700;font-size:10.5px;color:var(--red);letter-spacing:.4px}
.flower{left:664px;top:426px;width:107px;height:74px;background:radial-gradient(circle at 60% 70%,#3d72c2 0,#8fb0df 30%,var(--cream) 70%)}
.net-wt{left:505px;top:505px;width:200px;text-align:center;font-family:"Playfair Display",Georgia,serif;font-weight:700;font-size:11px;color:var(--ink);letter-spacing:.3px}

/* right panel */
.mini-mark{left:837px;top:256px;width:193px;display:flex;align-items:center;justify-content:center;gap:5px;font-family:"Cinzel",Georgia,serif;font-weight:600;font-size:14px;line-height:16px;color:var(--red);white-space:nowrap}
.mini-mark i{display:block;width:8px;height:8px;border-radius:50%;background:var(--red)}
.story{left:837px;top:287px;width:193px;font-family:"Playfair Display",Georgia,serif;font-style:italic;font-weight:700;font-size:10px;line-height:10.6px;color:#3a2418;text-align:justify}
.storage{left:834px;top:360px;width:201px;height:57px;background:linear-gradient(90deg,var(--blue-deep),var(--blue) 55%,var(--blue-deep));padding:4px 7px;font-family:"Playfair Display",Georgia,serif;font-weight:700;font-size:8.6px;line-height:8.8px;color:#fff;text-align:justify}
.batch-label{left:842px;top:438px;font-family:"Playfair Display",Georgia,serif;font-weight:700;font-size:6.5px;letter-spacing:.5px;color:var(--ink)}
.batch-field{left:908px;top:435px;width:113px;height:15px;background:#fdf3d2}
</style>
</head>
<body>
<div class="canvas">
  <svg class="label-shape" width="1200" height="676" viewBox="0 0 1200 676">
    <defs>
      <linearGradient id="frame" x1="0" y1="0" x2="1" y2="1">
        <stop offset="0" stop-color="#0f2f6e"/>
        <stop offset=".5" stop-color="#2a7ac6"/>
        <stop offset="1" stop-color="#0f2f6e"/>
      </linearGradient>
      <radialGradient id="paper" cx=".5" cy=".45" r=".7">
        <stop offset="0" stop-color="#ead6a8"/>
        <stop offset="1" stop-color="#dcbf8e"/>
      </radialGradient>
    </defs>
    <polygon fill="url(#frame)" points="135,195 388,195 388,149 605,123 822,149 822,195 1072,195 1072,484 822,484 822,530 605,556 388,530 388,484 135,484"/>
    <polygon fill="url(#paper)" points="144,204 397,204 397,157 605,132 813,157 813,204 1063,204 1063,475 813,475 813,522 605,547 397,522 397,475 144,475"/>
    <polygon fill="none" stroke="#f6c200" stroke-width="1.3" points="155,213 406,213 406,165 605,141 805,165 805,213 1055,213 1055,466 805,466 805,514 605,538 406,514 406,466 155,466"/>
    <rect x="144" y="436" width="280" height="13" fill="#f6c200"/>
    <rect x="785" y="436" width="278" height="13" fill="#f6c200"/>
  </svg>

  <section class="abs nutrition">
    <h2>Nutrition Facts</h2>
    <p class="servings">22 servings per container</p>
    <div class="row"><b>Serving size</b><b>1Tbsp (21g)</b></div>
    <div class="bar-thick"></div>
    <p class="amount">Amount per serving</p>
    <div class="calories"><span>Calories</span><span>60</span></div>
    <p class="dv">%Daily Value*</p>
    <div class="line"><span><b>Total Fat</b> 0g</span><b>0%</b></div>
    <div class="line"><span><b>Sodium</b> 0mg</span><b>0%</b></div>
    <div class="line"><span><b>Total Carbohydrate</b> 17g</span><b>6%</b></div>
    <div class="line sub"><span>Total Sugar 16g</span></div>
    <div class="line last"><span><b>Protein</b></span><b>0%</b></div>
    <p class="foot">Percent Daily Values are based on a 2,000 calorie diet.</p>
    <p class="ingredients"><b>Ingredients:</b> Honey</p>
  </section>

  <svg class="abs recycle" viewBox="0 0 14 14" aria-label="Recycle"><circle cx="7" cy="7" r="5" fill="none" stroke="#c2242f" stroke-width="2.2" stroke-dasharray="7 3"/></svg>
  <p class="abs order-note">Order more honey at:<span>www.corvalebees.com</span></p>

  <div class="abs brand-mark"><i></i>Corvale Bees</div>
  <h1 class="abs title farm">CORVALE FARMS</h1>
  <p class="abs title product">MAPLE SYRUP</p>

  <div class="abs ticket"></div>
  <div class="abs ticket-frame"></div>
  <div class="abs ticket-divider-v"></div>
  <div class="abs ticket-divider-h"></div>
  <p class="abs ticket-text"><em>Corvale Bees:</em> Pure, local honey and maple syrup from our family farm. Handcrafted with care, straight from our hives to your home.</p>
  <p class="abs ticket-url">WWW.CORVALEBEES.COM</p>
  <div class="abs flower" role="img" aria-label="Line drawing of a blue flower"></div>
  <p class="abs net-wt">NET WT 35.27 OZ (1 KG)</p>

  <div class="abs mini-mark"><i></i>Corvale Bees</div>
  <p class="abs story">Harvested from American bees, our raw wildflower honey is bottled in small batches with care. Corvale Bees: Pure, local honey and maple syrup from our family farm. Handcrafted with care, straight from our hives to your home.</p>
  <p class="abs storage">Store at room temperature. Raw honey never spoils but it may crystallize over time. To restore it smooth texture, simply warm the jar in hot water or leave in hot car during the day.</p>
  <p class="abs batch-label">BATCH NUMBER</p>
  <div class="abs batch-field"></div>
</div>
</body>
</html>
```